Logo and packaging design for a food brand: Amber Hollow

Dear designer,

I'm located in Vancouver, British Columbia, Canada, and I'm launching a brand of products made of beef tallow. It's called Amber Hollow. I'm ultimately looking for a designer that can help me build the brand and create a series of products.

Here is what I need at this point:

- A logo for Amber Hollow (playing with the letters A and H - sketch using ChatGPT attached)
- A packaging design for the PREMIUM WAGYU TALLOW - 235 ml (= 8 oz: https://www.jarvelo-supply.example/Product/Detail/K-40261M-TN/Jars/Clear-Straight-Sided-Glass-Jars-8-oz-Black-Plastic-Cap)
- Glass jar with a label all around it and a lid seal label
- Primary colours: black, white, gold
- Secondary colours if needed: Canada red and light grey
- Fonts: not specified, looking forward to your inputs on what works
- Please refer to our #1 competitor as reference: https://www.northbrimlarder.example/collections/products (we like their design style as well)
- #2 competitor to be used as reference: https://quellmoor.example/products/1-jar-14-0-oz-organic-grass-fed-beef-tallow

- Information for the packaging:
PREMIUM WAGYU BEEF TALLOW
100% PURE
(optional) PRODUCED IN CANADA
NUTRITIONAL VALUE (we don't have the numbers yet, but please create a placeholder/mockup for this section)
* You can also add more information following the example from our Competitor 01

- Please feel free to improve the logo, but keep the concept of Amber Hollow (or AH) + the face of a bull
- Finally, I'd also love to see two colour schemes: one dark and one bright - I hope it's not asking too much

Target Market(s)

North America

Industry/Entity Type

Food

Font styles to use
Sans Serif
Script

Colors
FFC000
F8CF3A
FAE287
FDF2CF
FEFAEE

Requirements
Must have
• Incorporate gold, black and white
Nice to have
• Play with the letters AH in the logo (company name: Amber Hollow)
Should not have
• Many colours

```html
<!DOCTYPE html>
<html lang="en">
<head>
<meta charset="UTF-8">
<title>Amber Hollow – Premium Wagyu Beef Tallow Label</title>
<link rel="stylesheet" href="https://fonts.googleapis.com/css2?family=Oswald:wght@500;700&family=Alfa+Slab+One&display=swap">
<style>
  :root {
    --backdrop: #e4e4e4;
    --label-black: #212121;
    --gold-light: #a99466;
    --gold-mid: #8b7448;
    --gold-dark: #5e4c2f;
    --ink-dark: #1c1c1c;
  }
  html, body {
    margin: 0;
    padding: 0;
    width: 1200px;
    height: 1200px;
    overflow: hidden;
    background: var(--backdrop);
  }
  .canvas {
    position: relative;
    width: 1200px;
    height: 1200px;
  }
  .label {
    position: absolute;
    left: 150px;
    top: 175px;
    width: 900px;
    height: 850px;
    background: var(--label-black);
    overflow: hidden;
  }
  .brand-vertical {
    position: absolute;
    left: 145px;
    top: 438px;
    transform: translate(-50%, -50%) rotate(-90deg);
    white-space: nowrap;
    font-family: "Alfa Slab One", serif;
    font-size: 66px;
    letter-spacing: 4px;
    color: var(--gold-mid);
  }
  .brand-mark {
    position: absolute;
    left: 588px;
    top: 110px;
    transform: translateX(-50%);
    display: flex;
    align-items: center;
    gap: 14px;
    white-space: nowrap;
  }
  .brand-mark__dot {
    width: 34px;
    height: 34px;
    border-radius: 50%;
    border: 3px solid var(--gold-mid);
    box-sizing: border-box;
  }
  .brand-mark__name {
    font-family: "Oswald", sans-serif;
    font-weight: 700;
    font-size: 36px;
    letter-spacing: 3px;
    color: var(--gold-mid);
  }
  .hero-art {
    position: absolute;
    left: 266px;
    top: 228px;
    width: 518px;
    height: 441px;
    border-radius: 40px;
    background: linear-gradient(160deg, var(--gold-light), var(--gold-mid) 55%, var(--gold-dark));
  }
  .product-name {
    position: absolute;
    left: 322px;
    top: 356px;
    font-family: "Oswald", sans-serif;
    font-weight: 700;
    color: var(--ink-dark);
    line-height: 1;
  }
  .product-name__premium {
    display: block;
    font-size: 74px;
    letter-spacing: 1px;
  }
  .product-name__row {
    display: flex;
    align-items: center;
    margin-top: 0;
  }
  .product-name__wagyu {
    font-size: 74px;
    letter-spacing: 6px;
  }
  .product-name__sub {
    display: flex;
    flex-direction: column;
    font-weight: 500;
    font-size: 26px;
    line-height: 0.95;
    margin-left: 6px;
  }
  .purity {
    position: absolute;
    left: 539px;
    top: 712px;
    transform: translateX(-50%);
    font-family: "Oswald", sans-serif;
    font-weight: 700;
    font-size: 48px;
    letter-spacing: 1px;
    color: var(--gold-mid);
    white-space: nowrap;
  }
  .origin-badge {
    position: absolute;
    left: 410px;
    top: 784px;
    width: 255px;
    height: 66px;
    border-radius: 14px 14px 0 0;
    background: linear-gradient(90deg, var(--gold-light), var(--gold-dark));
    display: flex;
    align-items: center;
    gap: 16px;
    padding-left: 26px;
    box-sizing: border-box;
  }
  .origin-badge__flag {
    display: block;
  }
  .origin-badge__text {
    font-family: "Oswald", sans-serif;
    font-weight: 700;
    font-size: 19px;
    line-height: 1;
    color: var(--ink-dark);
  }
</style>
</head>
<body>
<div class="canvas">
  <section class="label">
    <div class="brand-vertical">AMBER HOLLOW</div>

    <div class="brand-mark">
      <span class="brand-mark__dot"></span>
      <span class="brand-mark__name">AMBER HOLLOW</span>
    </div>

    <div class="hero-art" role="img" aria-label="Distressed gold silhouette of a standing bull in side profile with a curled tail"></div>

    <h1 class="product-name">
      <span class="product-name__premium">PREMIUM</span>
      <span class="product-name__row">
        <span class="product-name__wagyu">WAGYU</span>
        <span class="product-name__sub"><span>BEEF</span><span>TALLOW</span></span>
      </span>
    </h1>

    <div class="purity">100% PURE</div>

    <div class="origin-badge">
      <svg class="origin-badge__flag" width="54" height="30" viewBox="0 0 54 30" aria-hidden="true">
        <rect x="0" y="0" width="13" height="30" fill="#1c1c1c"/>
        <rect x="41" y="0" width="13" height="30" fill="#1c1c1c"/>
        <rect x="22" y="10" width="10" height="10" fill="#1c1c1c"/>
      </svg>
      <div class="origin-badge__text">PRODUCED<br>IN CANADA</div>
    </div>
  </section>
</div>
</body>
</html>
```